Post card for Tax Preparation Services

Beacon Ledger, a accounting and tax solution firm is in need of a postcard to send to people who have moved into the area in the last year. The goal is to market our tax preparation services. More information on our business and services can be found on our website: www.beaconledger-example.com

Return address:
4817 Maple Ridge Blvd
Bldg 300, Ste 410
Woodstock, GA 30189

Phone: (555) 013-4LED

Please submit copies of front and back design in one submisstion. Do not submit duplicate designs.

Target Market(s)

People who have moved within 2 miles of our office

Industry/Entity Type

Accounting

Colors
6b449b
fbee3e

Requirements
Must have
• Logo
• Schedule Online
• Mention this postcard Receive $25.00 off tax prep
• Colors Gold #c6A734 and Purple #5f1547 to match logo
Should not have
• No cartoony feel

```html
<!DOCTYPE html>
<html lang="en">
<head>
<meta charset="utf-8">
<title>Beacon Ledger – Tax Preparation Postcard</title>
<link rel="stylesheet" href="https://fonts.googleapis.com/css2?family=Roboto+Condensed:wght@400;700&family=Montserrat:wght@400;600;700&display=swap">
<style>
  :root {
    --purple: #5f1547;
    --purple-deep: #45103a;
    --gold: #c6a734;
    --ink: #2a2a2a;
    --paper: #ffffff;
    --stage: #e8e8e9;
    --rule: #c9c9c9;
  }
  * { box-sizing: border-box; margin: 0; padding: 0; }
  html, body { width: 1200px; height: 961px; overflow: hidden; }
  body { background: var(--stage); position: relative; }

  .postcard {
    position: absolute; left: 255px; width: 690px; height: 455px;
    background: var(--paper); overflow: hidden;
    box-shadow: 0 2px 8px rgba(0,0,0,.15);
  }
  .postcard--front { top: 17px; }
  .postcard--back { top: 489px; }
  .postcard__art { position: absolute; inset: 0; }
  .postcard > div, .postcard > p, .postcard > ul { position: absolute; }

  .brand { display: flex; align-items: center; gap: 9px; }
  .brand__mark { width: 26px; height: 26px; background: var(--gold); }
  .brand__name {
    font-family: "Roboto Condensed", sans-serif; font-weight: 700;
    font-size: 30px; color: var(--gold); letter-spacing: .5px; line-height: 1;
  }

  /* Front */
  .front-brand { left: 28px; top: 38px; }
  .service-title {
    left: 28px; top: 112px; font-family: "Roboto Condensed", sans-serif;
    font-weight: 700; font-size: 29px; line-height: 1.08; color: var(--ink);
  }
  .service-title .accent { color: var(--gold); }
  .tagline {
    left: 24px; top: 202px; font-family: "Roboto Condensed", sans-serif;
    font-size: 16px; color: #fff;
  }
  .service-list {
    left: 26px; top: 248px; list-style: none;
    font-family: "Roboto Condensed", sans-serif; font-size: 15px; color: #fff;
  }
  .service-list li { display: flex; align-items: center; gap: 9px; height: 19.5px; }
  .service-list svg { width: 11px; height: 11px; flex: none; }
  .offer {
    left: 294px; top: 281px; width: 102px; height: 102px;
    display: flex; flex-direction: column; align-items: center; justify-content: center;
    font-family: "Roboto Condensed", sans-serif; font-weight: 700; color: #fff; line-height: 1;
  }
  .offer__amount { font-size: 29px; white-space: nowrap; }
  .offer__amount small { font-size: 17px; }
  .offer__label { font-size: 21px; margin-top: 2px; white-space: nowrap; }
  .front-cta {
    left: 22px; top: 420px; font-family: "Roboto Condensed", sans-serif;
    font-weight: 700; font-size: 15px; color: var(--purple); white-space: nowrap;
  }
  .front-cta .gold { color: var(--gold); margin-left: 8px; }

  /* Back */
  .back-brand { left: 28px; top: 30px; }
  .back-brand .brand__name { font-family: "Montserrat", sans-serif; font-size: 24px; }
  .back-tagline {
    left: 26px; top: 104px; font-family: "Montserrat", sans-serif;
    font-weight: 700; font-size: 13px; color: #fff;
  }
  .intro {
    left: 26px; top: 140px; width: 360px; font-family: "Montserrat", sans-serif;
    font-size: 10.5px; line-height: 1.45; color: #fff;
  }
  .preparer {
    left: 160px; top: 258px; font-family: "Montserrat", sans-serif; color: #fff; font-size: 10.5px;
  }
  .preparer__heading { color: var(--gold); font-weight: 700; font-size: 12px; }
  .preparer__name { color: var(--gold); font-weight: 700; font-size: 12px; margin-top: 8px; }
  .preparer__line { display: flex; align-items: center; gap: 7px; margin-top: 4px; }
  .preparer__line svg { width: 12px; height: 12px; flex: none; }
  .back-cta {
    left: 160px; top: 412px; font-family: "Montserrat", sans-serif;
    font-weight: 700; font-size: 11px; color: var(--purple-deep); letter-spacing: .5px;
  }
  .back-call {
    left: 160px; top: 432px; font-family: "Montserrat", sans-serif;
    font-weight: 700; font-size: 15px; color: var(--purple-deep);
  }
</style>
</head>
<body>

<section class="postcard postcard--front">
  <svg class="postcard__art" viewBox="0 0 690 455" aria-hidden="true">
    <defs>
      <linearGradient id="panelFill" x1="0" y1="0" x2="1" y2="1">
        <stop offset="0" stop-color="#6a1a50"/><stop offset="1" stop-color="#4a0f3b"/>
      </linearGradient>
      <clipPath id="frontPhotoClip"><rect x="0" y="18" width="690" height="392"/></clipPath>
    </defs>
    <rect x="0" y="232" width="690" height="176" fill="url(#panelFill)"/>
    <rect x="0" y="190" width="238" height="40" fill="var(--gold)"/>
    <path d="M238 190 h6 a10 10 0 0 1 10 10 v30 h-16z" fill="var(--gold)"/>
    <g clip-path="url(#frontPhotoClip)">
      <circle cx="590" cy="212" r="262" fill="var(--gold)"/>
      <circle cx="590" cy="212" r="255" fill="#fff"/>
      <circle cx="590" cy="212" r="250" fill="var(--gold)"/>
    </g>
    <rect x="0" y="408" width="690" height="47" fill="#fff"/>
  </svg>
  <svg class="postcard__art" viewBox="0 0 690 455" role="img" aria-label="Photo of a café owner in an apron reading his tax papers over coffee">
    <defs>
      <linearGradient id="photoFill" x1="0" y1="0" x2="1" y2="1">
        <stop offset="0" stop-color="#3b302a"/><stop offset=".5" stop-color="#5a4636"/><stop offset="1" stop-color="#2f3f6a"/>
      </linearGradient>
      <clipPath id="frontPhotoClip2"><rect x="0" y="18" width="690" height="388"/></clipPath>
    </defs>
    <circle cx="590" cy="212" r="246" fill="url(#photoFill)" clip-path="url(#frontPhotoClip2)"/>
    <circle cx="345" cy="332" r="56" fill="#fff"/>
    <circle cx="345" cy="332" r="51" fill="var(--gold)"/>
  </svg>

  <div class="brand front-brand"><span class="brand__mark"></span><span class="brand__name">BEACON LEDGER</span></div>
  <div class="service-title"><span class="accent">TAX</span> PREPARATION<br>SERVICES</div>
  <div class="tagline">Take the stress out of tax time.</div>
  <ul class="service-list">
    <li><svg viewBox="0 0 12 12"><circle cx="6" cy="6" r="6" fill="#c6a734"/><path d="M5 3.5 7.5 6 5 8.5" stroke="#5f1547" stroke-width="1.6" fill="none"/></svg>Individual Tax Preparation</li>
    <li><svg viewBox="0 0 12 12"><circle cx="6" cy="6" r="6" fill="#c6a734"/><path d="M5 3.5 7.5 6 5 8.5" stroke="#5f1547" stroke-width="1.6" fill="none"/></svg>Business Tax Return Preparation</li>
    <li><svg viewBox="0 0 12 12"><circle cx="6" cy="6" r="6" fill="#c6a734"/><path d="M5 3.5 7.5 6 5 8.5" stroke="#5f1547" stroke-width="1.6" fill="none"/></svg>Gift &amp; Estate Tax Return Preparation</li>
    <li><svg viewBox="0 0 12 12"><circle cx="6" cy="6" r="6" fill="#c6a734"/><path d="M5 3.5 7.5 6 5 8.5" stroke="#5f1547" stroke-width="1.6" fill="none"/></svg>Partnership &amp; Corporate Tax Preparation</li>
    <li><svg viewBox="0 0 12 12"><circle cx="6" cy="6" r="6" fill="#c6a734"/><path d="M5 3.5 7.5 6 5 8.5" stroke="#5f1547" stroke-width="1.6" fill="none"/></svg>Estate and Succession Planning</li>
    <li><svg viewBox="0 0 12 12"><circle cx="6" cy="6" r="6" fill="#c6a734"/><path d="M5 3.5 7.5 6 5 8.5" stroke="#5f1547" stroke-width="1.6" fill="none"/></svg>Out-of-State Returns</li>
    <li><svg viewBox="0 0 12 12"><circle cx="6" cy="6" r="6" fill="#c6a734"/><path d="M5 3.5 7.5 6 5 8.5" stroke="#5f1547" stroke-width="1.6" fill="none"/></svg>Business Start-Ups</li>
  </ul>
  <div class="offer"><div class="offer__amount">$25<small> OFF</small></div><div class="offer__label">TAX PREP</div></div>
  <div class="front-cta">SCHEDULE YOUR APPOINTMENT<span class="gold">Call (555) 013-4LED or visit www.beaconledger-example.com</span></div>
</section>

<section class="postcard postcard--back">
  <svg class="postcard__art" viewBox="0 0 690 455" aria-hidden="true">
    <defs>
      <linearGradient id="backPanel" x1="0" y1="0" x2="1" y2="1">
        <stop offset="0" stop-color="#6a1a50"/><stop offset="1" stop-color="#45103a"/>
      </linearGradient>
    </defs>
    <path d="M0 112 H410 C480 150 502 300 472 428 H0Z" fill="var(--gold)"/>
    <path d="M0 118 H404 C471 156 492 300 463 424 H0Z" fill="#fff"/>
    <path d="M0 122 H400 C465 160 484 300 456 420 H0Z" fill="url(#backPanel)"/>
    <path d="M0 96 H290 a10 10 0 0 1 10 10 v14 a10 10 0 0 1 -10 10 H0Z" fill="var(--gold)"/>
    <path d="M150 406 H470 a6 6 0 0 1 6 6 v10 a6 6 0 0 1 -6 6 H150Z" fill="var(--gold)"/>
    <g stroke="var(--rule)" stroke-width="1.2">
      <line x1="510" y1="70" x2="670" y2="70"/>
      <line x1="510" y1="110" x2="670" y2="110"/>
      <line x1="510" y1="150" x2="670" y2="150"/>
      <line x1="510" y1="190" x2="670" y2="190"/>
    </g>
  </svg>
  <svg class="postcard__art" viewBox="0 0 690 455" role="img" aria-label="Portrait photo of the tax preparer">
    <rect x="18" y="300" width="124" height="116" rx="4" fill="#8a6b5a"/>
  </svg>

  <div class="brand back-brand"><span class="brand__mark"></span><span class="brand__name">BEACON LEDGER</span></div>
  <div class="back-tagline">Take the stress out of tax time</div>
  <p class="intro">Preparing and planning for taxes is often a stressful and complicated endeavor for most people. At Beacon Ledger, our tax accountants have the expertise that is needed to help you file your returns while also helping you to minimize your tax liability with careful planning.</p>
  <div class="preparer">
    <div class="preparer__heading">CHOOSE A TAX PREPARER</div>
    <div>Take the stress out of tax time.</div>
    <div class="preparer__name">Dana Whitfield EA</div>
    <div class="preparer__line"><svg viewBox="0 0 12 12"><circle cx="6" cy="6" r="6" fill="#c6a734"/><path d="M4 3.2c.5 2.6 2.2 4.5 4.8 5.3l.6-1.2-1.5-.7-.6.6c-.9-.5-1.6-1.2-2-2.1l.6-.6-.7-1.5z" fill="#fff"/></svg>(555) 013-4LED</div>
    <div class="preparer__line"><svg viewBox="0 0 12 12"><circle cx="6" cy="6" r="6" fill="#c6a734"/><rect x="3" y="4" width="6" height="4.2" fill="none" stroke="#fff" stroke-width=".9"/><path d="M3 4l3 2.3L9 4" fill="none" stroke="#fff" stroke-width=".9"/></svg>dana.whitfield@beaconledger-example.com</div>
    <div class="preparer__line"><svg viewBox="0 0 12 12"><circle cx="6" cy="6" r="6" fill="#c6a734"/><circle cx="6" cy="6" r="3" fill="none" stroke="#fff" stroke-width=".9"/><path d="M3 6h6M6 3c-1.4 1.8-1.4 4.2 0 6M6 3c1.4 1.8 1.4 4.2 0 6" fill="none" stroke="#fff" stroke-width=".7"/></svg>www.beaconledger-example.com</div>
  </div>
  <div class="back-cta">SCHEDULE YOUR APPOINTMENT</div>
  <div class="back-call">Call (555) 013-4LED</div>
</section>

</body>
</html>
```